Erotik Online Shop
Zielgruppe
Kunden des Online Shops, vorzugsweise schwule Männer wobei der Shop auch die hetero Ziegruppe bedienen bzw. befriedigen kann.
Aufgabenstellung
Für den Relounch unserers Online Shops benötigen wir mehrer Grafiken für die Startseite des Shops sowie eventuell einen Überabreitung unseres Logos.

```html
<!DOCTYPE html>
<html lang="de">
<head>
<meta charset="utf-8">
<title>Flirtwerk7 – Startseiten-Banner</title>
<link rel="stylesheet" href="https://fonts.googleapis.com/css2?family=Open+Sans:wght@300;400;600&display=swap">
<style>
  :root {
    --bg-deep: #050505;
    --bg-mid: #1a1a1a;
    --bg-light: #3b3b3b;
    --accent-red: #d0232c;
    --text-white: #ffffff;
    --photo-dark: #2b1b14;
    --photo-mid: #7a4a34;
    --photo-warm: #c07f5c;
    --photo-light: #e0a987;
  }
  html, body {
    margin: 0;
    padding: 0;
    width: 1200px;
    height: 688px;
    overflow: hidden;
    background: #ffffff;
  }
  .banner {
    position: relative;
    width: 1200px;
    height: 688px;
    overflow: hidden;
    border-radius: 0 22px 22px 0;
    background: linear-gradient(90deg, var(--bg-deep) 0%, var(--bg-deep) 28%, var(--bg-mid) 55%, var(--bg-light) 100%);
    font-family: "Open Sans", Arial, sans-serif;
  }
  .hero-photo {
    position: absolute;
    top: 0;
    right: 0;
    width: 640px;
    height: 688px;
    background:
      linear-gradient(180deg, var(--photo-dark) 0%, rgba(43,27,20,0.6) 22%, rgba(43,27,20,0) 40%),
      linear-gradient(160deg, var(--photo-light) 20%, var(--photo-warm) 55%, var(--photo-mid) 100%);
    -webkit-mask-image: linear-gradient(90deg, transparent 0%, rgba(0,0,0,0.6) 18%, #000 34%);
            mask-image: linear-gradient(90deg, transparent 0%, rgba(0,0,0,0.6) 18%, #000 34%);
  }
  .headline {
    position: absolute;
    left: 86px;
    top: 118px;
    margin: 0;
    color: var(--accent-red);
    font-weight: 300;
    font-size: 60px;
    line-height: 74px;
    letter-spacing: -0.5px;
  }
  .tagline {
    position: absolute;
    left: 91px;
    top: 346px;
    margin: 0;
    color: var(--text-white);
    font-weight: 300;
    font-size: 31px;
    letter-spacing: -0.3px;
  }
  .brand-name {
    position: absolute;
    left: 90px;
    top: 572px;
    margin: 0;
    color: var(--accent-red);
    font-weight: 600;
    font-size: 58px;
    letter-spacing: -1px;
  }
</style>
</head>
<body>
  <div class="banner">
    <div class="hero-photo" role="img" aria-label="Foto eines Mannes mit geschlossenen Augen, der genüsslich in eine Erdbeere beißt"></div>
    <h1 class="headline">Süße Frucht<br>oder harte Nuss?</h1>
    <p class="tagline">Das Richtige für jede Vorliebe.</p>
    <p class="brand-name">Flirtwerk7</p>
  </div>
</body>
</html>
```